Business Card Design for Occupational Medicine Start Up Company

We need to design a professional business card. We are a healthcare company providing occupational medicine services to blue collar industries. We are professional, efficient and high quality service providers.

Target Market(s)

Blue Collar Industry: Shipbuilding, Ports, Trucking Companies; The Executives and Safety Officers for these companies

Industry/Entity Type

Healthcare

Contact Information for Business Card

Logo, Name, Title, Email, Phone

Other font styles liked:
• Please match our Brand Guide

Requirements
Must have
• Our Company Colors and Logo

```html
<!DOCTYPE html>
<html lang="en">
<head>
<meta charset="utf-8">
<title>Shoreline Works Clinics – Business Card</title>
<link rel="stylesheet" href="https://fonts.googleapis.com/css2?family=Montserrat:wght@700&family=Poppins:wght@300;400;600;700&display=swap">
<style>
  :root {
    --brand-blue: #26a9e0;
    --brand-navy: #2e3192;
    --brand-orange: #f7ae44;
    --tint-blue: #7cc3e3;
    --tint-orange: #fbd9a6;
    --tint-grey: #ececee;
    --ink: #1d1d1f;
    --paper: #ffffff;
    --backdrop: #f3f3f3;
  }
  * { box-sizing: border-box; margin: 0; padding: 0; }
  html, body { width: 670px; height: 1200px; overflow: hidden; }
  body { background: var(--backdrop); position: relative; font-family: "Poppins", sans-serif; }

  .card {
    position: absolute; left: 100px; width: 469px; height: 268px;
    background: var(--paper); overflow: hidden;
    box-shadow: 0 6px 14px rgba(0,0,0,0.22);
  }
  .card--front { top: 300px; }
  .card--back { top: 632px; }

  /* Front */
  .front__field {
    position: absolute; left: 0; top: 0; width: 100%; height: 209px;
    background: var(--brand-blue);
  }
  .front__stripe {
    position: absolute; left: 0; top: 209px; width: 100%; height: 6px;
    background: var(--brand-orange);
  }
  .front__mark {
    position: absolute; left: 50%; top: 56px; width: 52px; height: 52px;
    margin-left: -26px; border-radius: 50%; background: var(--paper);
  }
  .front__name {
    position: absolute; left: 0; top: 124px; width: 100%; text-align: center;
    font-family: "Montserrat", sans-serif; font-weight: 700; font-size: 25px;
    line-height: 1.15; color: var(--paper); letter-spacing: 0.5px;
  }
  .front__corner {
    position: absolute; top: 215px; width: 78px; height: 53px;
  }
  .front__corner--left { left: 0; background: linear-gradient(90deg, var(--tint-grey), rgba(236,236,238,0)); }
  .front__corner--right { right: 0; background: linear-gradient(270deg, var(--tint-grey), rgba(236,236,238,0)); }
  .front__web {
    position: absolute; left: 0; top: 229px; width: 100%; text-align: center;
    font-weight: 700; font-size: 14px; letter-spacing: 3.6px; color: var(--ink);
  }
  .front__web .accent { color: var(--brand-blue); }

  /* Back */
  .back__corner { position: absolute; }
  .back__corner--top { right: 0; top: 0; width: 150px; height: 75px;
    background: linear-gradient(225deg, var(--tint-blue), rgba(124,195,227,0) 75%); }
  .back__corner--bottom { right: 0; bottom: 0; width: 160px; height: 90px;
    background: linear-gradient(315deg, var(--tint-blue), rgba(124,195,227,0) 75%); }
  .back__corner--left { left: 0; bottom: 0; width: 120px; height: 55px;
    background: linear-gradient(45deg, var(--tint-orange), rgba(251,217,166,0) 70%); }

  .person { position: absolute; left: 27px; top: 49px; }
  .person__name {
    font-size: 21px; font-weight: 400; color: var(--brand-navy); line-height: 1.1;
    padding-bottom: 2px; border-bottom: 1px solid var(--brand-orange); display: inline-block;
  }
  .person__name strong { font-weight: 600; }
  .person__title {
    margin-top: 1px; font-size: 14px; font-weight: 700; color: var(--brand-navy);
  }

  .contacts { position: absolute; left: 0; top: 135px; list-style: none; }
  .contact { display: flex; align-items: center; height: 21px; margin-bottom: 6.5px; }
  .contact__tab {
    width: 47px; height: 21px; background: var(--brand-blue);
    border-radius: 0 3px 3px 0; display: flex; align-items: center; justify-content: flex-end;
    padding-right: 9px;
  }
  .contact__tab svg { width: 13px; height: 13px; }
  .contact__text { margin-left: 11px; font-size: 11px; font-weight: 400; color: var(--ink); }
  .contact__text--wide { letter-spacing: 2.2px; font-weight: 300; }

  .back__brand {
    position: absolute; left: 278px; top: 72px; width: 180px; text-align: center;
  }
  .back__mark {
    width: 46px; height: 46px; border-radius: 50%; background: var(--brand-navy);
    margin: 0 auto 10px;
  }
  .back__name {
    font-family: "Montserrat", sans-serif; font-weight: 700; font-size: 17px;
    line-height: 1.15; color: var(--brand-navy);
  }
</style>
</head>
<body>

<section class="card card--front" aria-label="Business card front">
  <div class="front__field"></div>
  <div class="front__mark"></div>
  <p class="front__name">SHORELINE WORKS<br>CLINICS</p>
  <div class="front__stripe"></div>
  <div class="front__corner front__corner--left" role="img" aria-label="Faint grey medical cross pattern"></div>
  <div class="front__corner front__corner--right" role="img" aria-label="Faint grey medical cross pattern"></div>
  <p class="front__web">www.<span class="accent">shorelineworksclinics</span>.com</p>
</section>

<section class="card card--back" aria-label="Business card back">
  <div class="back__corner back__corner--top" role="img" aria-label="Light blue medical cross pattern"></div>
  <div class="back__corner back__corner--bottom" role="img" aria-label="Light blue medical cross pattern"></div>
  <div class="back__corner back__corner--left" role="img" aria-label="Pale orange medical cross pattern"></div>

  <div class="person">
    <h1 class="person__name">Daniel <strong>Reyes</strong></h1>
    <p class="person__title">Executive Officer</p>
  </div>

  <ul class="contacts">
    <li class="contact">
      <span class="contact__tab">
        <svg viewBox="0 0 24 24" aria-hidden="true"><path fill="#2e3192" d="M6.6 10.8a15.1 15.1 0 0 0 6.6 6.6l2.2-2.2c.3-.3.7-.4 1-.2 1.1.4 2.3.6 3.6.6.6 0 1 .4 1 1V20c0 .6-.4 1-1 1A17 17 0 0 1 3 4c0-.6.4-1 1-1h3.5c.6 0 1 .4 1 1 0 1.3.2 2.5.6 3.6.1.3 0 .7-.2 1z"/></svg>
      </span>
      <span class="contact__text">(555) 014-2290</span>
    </li>
    <li class="contact">
      <span class="contact__tab">
        <svg viewBox="0 0 24 24" aria-hidden="true"><rect x="2" y="5" width="20" height="14" fill="#2e3192"/><path d="M2 5l10 8 10-8" fill="none" stroke="#26a9e0" stroke-width="1.6"/></svg>
      </span>
      <span class="contact__text">reyes.daniel@mailbox.com</span>
    </li>
    <li class="contact">
      <span class="contact__tab">
        <svg viewBox="0 0 24 24" aria-hidden="true"><circle cx="12" cy="12" r="10" fill="#2e3192"/><g fill="none" stroke="#26a9e0" stroke-width="1.3"><ellipse cx="12" cy="12" rx="4.5" ry="10"/><path d="M2 12h20M4 7h16M4 17h16M12 2v20"/></g></svg>
      </span>
      <span class="contact__text contact__text--wide">www.shorelineworksclinics.com</span>
    </li>
  </ul>

  <div class="back__brand">
    <div class="back__mark"></div>
    <p class="back__name">SHORELINE WORKS<br>CLINICS</p>
  </div>
</section>

</body>
</html>
```